Media Banner

Create a banner similar to the one in the link below showing the various media publications (TVQRN, Marlowby Ledger, Kite Wire, Pellanstroud Bulletin) and then link to "More News..."

https://www.loanvistra.com/

The bar on loan vistra is blue. Please make this bar organe to match this site:
www.bramfieldlegal.com
The bar will be used on this cite to run accross the page.

Industry/Entity Type

Graphic Design

```html
<!DOCTYPE html>
<html lang="en">
<head>
<meta charset="utf-8">
<title>Bramfield Firm – Employment and Injury Attorneys</title>
<link href="https://fonts.googleapis.com/css2?family=PT+Sans:wght@400;700&display=swap" rel="stylesheet">
<style>
:root{
  --page-bg:#333333;
  --nav-bg:#333333;
  --crumb-bg:#454545;
  --paper:#ffffff;
  --ink:#333333;
  --muted:#999999;
  --nav-text:#bdbdbd;
  --orange:#e8741f;
  --orange-light:#f28c3a;
  --orange-dark:#d9631a;
  --social:#cfcfcf;
  --divider:#e3e3e3;
  --field-border:#cfcfcf;
  --sidebar:#5b5b5b;
  --chat-green:#2fb54a;
}
*{box-sizing:border-box;margin:0;padding:0}
html,body{width:1200px;height:907px;overflow:hidden}
body{background:var(--page-bg);font-family:"PT Sans",Arial,sans-serif;color:var(--ink);position:relative}
.abs{position:absolute}

.site-header{left:123px;top:0;width:948px;height:162px;background:var(--paper)}
.site-title{left:33px;top:28px;font-size:30px;font-weight:700;letter-spacing:.2px;color:var(--ink)}
.site-tagline{left:33px;top:61px;font-size:12.5px;color:#8a8a8a}
.header-phone{right:34px;top:30px;font-size:13.5px;font-weight:700}
.header-eval{right:34px;top:70px;font-size:12.5px;text-transform:uppercase}
.social-row{left:720px;top:89px;display:flex;gap:10px}
.social-row span{width:30px;height:30px;background:var(--social);border-radius:2px}

.main-nav{left:123px;top:162px;width:948px;height:108px;background:var(--nav-bg)}
.nav-item{font-size:13px;text-transform:uppercase;color:var(--nav-text);letter-spacing:.2px}
.nav-item.is-current{color:#fff}
.nav-marker{left:32px;top:0;width:0;height:0;border-left:5px solid transparent;border-right:5px solid transparent;border-top:7px solid #fff}

.breadcrumb{left:123px;top:270px;width:948px;height:47px;background:var(--crumb-bg);box-shadow:0 2px 3px rgba(0,0,0,.45);color:var(--nav-text);font-size:11.5px;padding:15px 0 0 19px}

.content{left:123px;top:319px;width:948px;height:415px;background:repeating-linear-gradient(90deg,#fff 0 2px,#f7f7f7 2px 3px)}
.divider{width:3px;background:var(--divider)}
.art{background:linear-gradient(#1b1b1b,#000)}
.service-title{font-size:19px;font-weight:700;text-align:center;text-transform:uppercase;width:100%}
.service-text{font-size:13px;line-height:21.5px;color:var(--muted);text-align:center}
.btn{display:flex;align-items:center;justify-content:center;background:linear-gradient(var(--orange-light),var(--orange-dark));color:#fff;font-size:11.5px;border-radius:2px;box-shadow:0 1px 2px rgba(0,0,0,.25)}

.form-title{font-size:12.5px;font-weight:700;text-transform:uppercase}
.form-label{font-size:12px;font-weight:700}
.form-label b{color:#d94c1a;font-weight:700}
.field{background:#fff;border:1px solid var(--field-border);border-radius:2px;box-shadow:inset 0 1px 2px rgba(0,0,0,.06)}
.field-hint{font-size:12.5px;color:#555}

.media-bar{left:123px;top:734px;width:948px;height:44px;background:linear-gradient(var(--orange-light),var(--orange) 55%,var(--orange-dark));box-shadow:0 2px 3px rgba(0,0,0,.35);color:#fff}
.media-bar .label{left:21px;top:13px;font-size:13.5px}
.outlet{top:11px;font-size:17px;font-weight:700;color:#fff;white-space:nowrap}
.more-news{right:28px;top:13px;font-size:13.5px;font-weight:700;color:#2a2a2a;text-decoration:underline}

.lower{left:123px;top:778px;width:948px;height:129px;background:var(--paper)}
.page-heading{left:33px;top:31px;font-size:29px;font-weight:700}
.sub-heading{left:33px;top:88px;font-size:24px;font-weight:700}
.sidebar{left:632px;top:0;width:316px;height:129px;background:repeating-linear-gradient(45deg,#5f5f5f 0 2px,#575757 2px 4px)}
.search{left:33px;top:33px;width:249px;height:43px;background:#fff;border:1px solid #ddd;font-size:11.5px;color:#888;padding:13px 0 0 12px}
.sidebar-strip{left:0;top:112px;width:316px;height:17px;background:#e4e4e4}

.chat{left:0;top:838px;width:139px;height:53px;background:#fff;border:1px solid #bbb;border-left:none;border-radius:0 4px 4px 0;font-size:9px;line-height:10px;color:#222;overflow:hidden}
.chat-close{right:4px;top:3px;width:10px;height:10px;border:1px solid #777;border-radius:50%}
.chat-btn{left:66px;top:34px;width:70px;height:15px;background:var(--chat-green);border-radius:3px;color:#fff;font-size:9.5px;display:flex;align-items:center;justify-content:center}
</style>
</head>
<body>

<header class="site-header abs">
  <div class="site-title abs">BRAMFIELD FIRM</div>
  <div class="site-tagline abs">Employment and Injury Attorneys</div>
  <div class="header-phone abs">555-014-2000</div>
  <div class="header-eval abs">Free Case Evaluation</div>
  <div class="social-row abs"><span></span><span></span><span></span><span></span><span></span></div>
</header>

<nav class="main-nav abs">
  <div class="nav-marker abs"></div>
  <div class="nav-item is-current abs" style="left:19px;top:23px">Home</div>
  <div class="nav-item abs" style="left:97px;top:23px">Firm</div>
  <div class="nav-item abs" style="left:170px;top:23px">Blog</div>
  <div class="nav-item abs" style="left:245px;top:23px">Press</div>
  <div class="nav-item abs" style="left:324px;top:23px">Client Reviews</div>
  <div class="nav-item abs" style="left:463px;top:23px">Legal Fees</div>
  <div class="nav-item abs" style="left:572px;top:23px">Contact</div>
  <div class="nav-item abs" style="right:24px;top:23px">January 12, 2014</div>
  <div class="nav-item abs" style="left:19px;top:71px">Employee Rights Guide</div>
  <div class="nav-item abs" style="left:210px;top:71px">Types of Employment Cases</div>
</nav>

<div class="breadcrumb abs">The Bramfield Firm, PC</div>

<main class="content abs">
  <div class="divider abs" style="left:313px;top:0;height:370px"></div>
  <div class="divider abs" style="left:628px;top:0;height:328px"></div>

  <section class="service abs" style="left:0;top:0;width:313px;height:370px">
    <div class="art abs" role="img" aria-label="Icon of an office worker in a suit and tie" style="left:108px;top:34px;width:98px;height:112px;border-radius:40px 40px 6px 6px"></div>
    <div class="service-title abs" style="top:174px">Employment Cases</div>
    <div class="service-text abs" style="left:20px;width:273px;top:209px">Have you been fired, harassed, cheated out of pay or otherwise kicked around at work? Give us a ...</div>
    <a class="btn abs" style="left:84px;top:291px;width:142px;height:46px">Read More</a>
  </section>

  <section class="service abs" style="left:316px;top:0;width:312px;height:370px">
    <div class="art abs" role="img" aria-label="Icon of two cars in a collision" style="left:58px;top:39px;width:201px;height:76px;border-radius:14px"></div>
    <div class="service-title abs" style="top:133px">Personal Injury Cases</div>
    <div class="service-text abs" style="left:30px;width:252px;top:169px">All personal injury cases are handled on a contingent fee basis. Here are the types of cases we ...</div>
    <a class="btn abs" style="left:84px;top:250px;width:142px;height:46px">See More</a>
  </section>

  <form class="contact abs" style="left:631px;top:0;width:317px;height:415px">
    <div class="form-title abs" style="left:0;width:300px;text-align:center;top:34px">Contact Us</div>
    <div class="form-label abs" style="left:33px;top:71px">Name <b>*</b></div>
    <div class="field abs" style="left:117px;top:69px;width:74px;height:44px"></div>
    <div class="field abs" style="left:197px;top:69px;width:72px;height:44px"></div>
    <div class="field-hint abs" style="left:117px;top:119px">First</div>
    <div class="field-hint abs" style="left:197px;top:119px">Last</div>
    <div class="form-label abs" style="left:33px;top:156px">Email <b>*</b></div>
    <div class="field abs" style="left:117px;top:153px;width:85px;height:45px"></div>
    <div class="form-label abs" style="left:33px;top:215px">Number</div>
    <div class="field abs" style="left:117px;top:212px;width:85px;height:45px"></div>
    <div class="form-label abs" style="left:33px;top:273px">Details</div>
    <div class="field abs" style="left:117px;top:271px;width:153px;height:65px"></div>
    <a class="btn abs" style="left:109px;top:363px;width:79px;height:42px">SUBMIT</a>
  </form>
</main>

<div class="media-bar abs">
  <div class="label abs">As seen In:</div>
  <div class="outlet abs" style="left:110px">TVQRN</div>
  <div class="outlet abs" style="left:246px">Fundhaven</div>
  <div class="outlet abs" style="left:354px">The Harbor Street Gazette</div>
  <div class="outlet abs" style="left:574px">Nation Daily</div>
  <div class="outlet abs" style="left:727px">KXN</div>
  <a class="more-news abs">More News...</a>
</div>

<section class="lower abs">
  <h1 class="page-heading abs">NY Employment &amp; Personal Injury Lawyers</h1>
  <h2 class="sub-heading abs">Free Case Evaluation</h2>
  <aside class="sidebar abs">
    <div class="search abs">Search this website...</div>
    <div class="sidebar-strip abs"></div>
  </aside>
</section>

<div class="chat abs">
  <div class="abs" style="left:-3px;top:3px;font-size:10px">Specialist Available</div>
  <div class="abs" style="left:-3px;top:14px;width:122px">ive Specialist here with the</div>
  <div class="abs" style="left:-3px;top:24px;width:122px">ramfield Firm. How may I assist</div>
  <div class="abs" style="left:-3px;top:34px">ou?</div>
  <div class="chat-close abs"></div>
  <div class="chat-btn abs">Start Chat</div>
</div>

</body>
</html>
```